Breast Cancer Stickers

Hi,
i would like a of small design for a breast cancer awareness campaign. please check attached picture this is the size and font i want. these will be stickers. Then i would like a little pink ribbon after each dot. so there will be four design please find below colors, slogans, etc..
1 I PINK I CAN. (Off white Background, Light Pink Font)
Never give up.
2 PINK POWER. (Black Background, Bright Pink Font)
Theres Always hope
3 POSITIVELY PINK. ( Light Pink Background, Off white Font)
Stay Positive
4 TURN UP THE PINK. (Bright Pink Background, Black font)
fight on.
Campaign

```html
<!DOCTYPE html>
<html lang="en">
<head>
<meta charset="utf-8">
<title>Breast Cancer Awareness Stickers</title>
<link rel="stylesheet" href="https://fonts.googleapis.com/css2?family=Inter:wght@600;700&display=swap">
<style>
  :root {
    --canvas: #a7a8ab;
    --off-white: #f6f8e6;
    --light-pink: #f3879b;
    --soft-pink: #f08aa0;
    --bright-pink: #ee3a96;
    --black: #000000;
  }
  html, body {
    margin: 0;
    padding: 0;
    width: 1042px;
    height: 1200px;
    overflow: hidden;
    background: var(--canvas);
    font-family: "Inter", "Helvetica Neue", Arial, sans-serif;
  }
  .sheet {
    position: relative;
    width: 1042px;
    height: 1200px;
  }
  .sticker {
    position: absolute;
    width: 350px;
    height: 350px;
    box-sizing: border-box;
  }
  .sticker--cream  { left: 143px; top: 250px; background: var(--off-white);  color: var(--soft-pink); }
  .sticker--black  { left: 546px; top: 250px; background: var(--black);      color: var(--bright-pink); }
  .sticker--pink   { left: 143px; top: 650px; background: var(--light-pink); color: var(--off-white); }
  .sticker--bright { left: 546px; top: 650px; background: var(--bright-pink); color: var(--black); }

  .slogan {
    position: absolute;
    margin: 0;
  }
  .slogan__headline {
    display: block;
    font-weight: 700;
    font-size: 61px;
    line-height: 0.9;
    letter-spacing: -0.005em;
  }
  .slogan__tagline {
    display: block;
    margin-top: 6px;
    font-weight: 700;
    font-size: 22.5px;
    letter-spacing: 0;
  }
  .sticker--cream .slogan  { left: 40px; top: 88px; }
  .sticker--black .slogan  { left: 44px; top: 82px; }
  .sticker--pink .slogan   { left: 30px; top: 74px; }
  .sticker--bright .slogan { left: 47px; top: 54px; }
  .sticker--bright .slogan__tagline { margin-top: 2px; }

  .ribbon {
    display: inline-block;
    width: 26px;
    height: 54px;
    margin-left: 2px;
    vertical-align: -10px;
    transform: rotate(12deg);
  }
  .ribbon path { fill: currentColor; }

  .partners {
    position: absolute;
    right: 16px;
    bottom: 20px;
    display: flex;
    align-items: center;
    gap: 12px;
    font-weight: 600;
    font-size: 11px;
    letter-spacing: 0.01em;
  }
</style>
</head>
<body>
<main class="sheet">

  <section class="sticker sticker--cream" aria-label="I Pink I Can sticker">
    <h2 class="slogan">
      <span class="slogan__headline">I Pink<br>I Can.<svg class="ribbon" viewBox="0 0 20 40" aria-hidden="true"><path d="M10 1C5 1 3 5 4.5 10L14 38l4-2L9.5 12C9 10 9 7 10 5c1 2 1 5 .5 7L2 36l4 2 9.5-28C17 5 15 1 10 1z"/></svg></span>
      <span class="slogan__tagline">Never give up.</span>
    </h2>
    <div class="partners">
      <span class="partner">Kindred Care</span>
      <span class="partner">Hope Alliance</span>
    </div>
  </section>

  <section class="sticker sticker--black" aria-label="Pink Power sticker">
    <h2 class="slogan">
      <span class="slogan__headline">Pink<br>Power.<svg class="ribbon" viewBox="0 0 20 40" aria-hidden="true"><path d="M10 1C5 1 3 5 4.5 10L14 38l4-2L9.5 12C9 10 9 7 10 5c1 2 1 5 .5 7L2 36l4 2 9.5-28C17 5 15 1 10 1z"/></svg></span>
      <span class="slogan__tagline">There’s always hope.</span>
    </h2>
    <div class="partners">
      <span class="partner">Kindred Care</span>
      <span class="partner">Hope Alliance</span>
    </div>
  </section>

  <section class="sticker sticker--pink" aria-label="Positively Pink sticker">
    <h2 class="slogan">
      <span class="slogan__headline">positively<br>pink.<svg class="ribbon" viewBox="0 0 20 40" aria-hidden="true"><path d="M10 1C5 1 3 5 4.5 10L14 38l4-2L9.5 12C9 10 9 7 10 5c1 2 1 5 .5 7L2 36l4 2 9.5-28C17 5 15 1 10 1z"/></svg></span>
      <span class="slogan__tagline">Stay positive.</span>
    </h2>
    <div class="partners">
      <span class="partner">Kindred Care</span>
      <span class="partner">Hope Alliance</span>
    </div>
  </section>

  <section class="sticker sticker--bright" aria-label="Turn Up the Pink sticker">
    <h2 class="slogan">
      <span class="slogan__headline">Turn<br>Up the<br>Pink.<svg class="ribbon" viewBox="0 0 20 40" aria-hidden="true"><path d="M10 1C5 1 3 5 4.5 10L14 38l4-2L9.5 12C9 10 9 7 10 5c1 2 1 5 .5 7L2 36l4 2 9.5-28C17 5 15 1 10 1z"/></svg></span>
      <span class="slogan__tagline">Fight on.</span>
    </h2>
    <div class="partners">
      <span class="partner">Kindred Care</span>
      <span class="partner">Hope Alliance</span>
    </div>
  </section>

</main>
</body>
</html>
```